Business Card Design

I am a RN and a Case Manager at a hospital. I would like some medical design

Industry/Entity Type

Medical

Contact Information for Business Card

Rosalind K Whitcombe, BSN, RN/BA Sociology
Case Manager
Phone: Home 8174920618 Cell 8173061597

```html
<!DOCTYPE html>
<html lang="en">
<head>
<meta charset="utf-8">
<title>Rosalind K Whitcombe – Business Card</title>
<link rel="stylesheet" href="https://fonts.googleapis.com/css2?family=Josefin+Sans:wght@700&family=Archivo:wght@500&display=swap">
<style>
  :root {
    --green: #8cb14b;
    --green-soft: #a9c776;
    --ink: #111111;
    --paper: #f1f1ef;
    --paper-shade: #e4e4e2;
  }
  * { margin: 0; padding: 0; box-sizing: border-box; }
  html, body { width: 1200px; height: 683px; overflow: hidden; background: var(--paper); }
  .card {
    position: relative;
    width: 1200px;
    height: 683px;
    overflow: hidden;
    background: radial-gradient(ellipse at 40% 40%, #f6f6f4 0%, var(--paper) 55%, var(--paper-shade) 100%);
  }
  .edge-band {
    position: absolute; left: 0; top: 0;
    width: 41px; height: 683px;
    background: var(--green);
  }
  .nurse-emblem {
    position: absolute; left: 100px; top: 10px;
    width: 140px; height: 192px;
  }
  .medical-emblem {
    position: absolute; left: 800px; top: 0;
    width: 400px; height: 683px;
  }
  .name {
    position: absolute; left: 103px; top: 240px;
    font-family: "Josefin Sans", sans-serif;
    font-weight: 700;
    font-variant: small-caps;
    font-size: 53px;
    letter-spacing: 1px;
    color: var(--green);
    white-space: nowrap;
  }
  .credentials {
    position: absolute; left: 103px; top: 313px;
    font-family: "Archivo", sans-serif;
    font-weight: 500;
    font-size: 38px;
    line-height: 44px;
    text-transform: uppercase;
    color: var(--ink);
    white-space: nowrap;
  }
  .contact-line {
    position: absolute; left: 92px;
    display: flex; align-items: center;
    font-family: "Archivo", sans-serif;
    font-weight: 500;
    font-size: 38px;
    letter-spacing: 2px;
    color: var(--ink);
    white-space: nowrap;
  }
  .contact-line.cell { top: 456px; }
  .contact-line.home { top: 534px; }
  .contact-icon { width: 50px; height: 58px; margin-right: 34px; }
</style>
</head>
<body>
<div class="card">
  <div class="edge-band"></div>

  <svg class="nurse-emblem" viewBox="0 0 140 192" role="img" aria-label="Illustration of a nurse with cap and stethoscope">
    <rect x="0" y="0" width="140" height="192" rx="28" fill="var(--green)" opacity="0.85"/>
  </svg>

  <svg class="medical-emblem" viewBox="0 0 400 683" role="img" aria-label="Large winged medical staff emblem, the caduceus, in green">
    <defs>
      <linearGradient id="emblemTone" x1="0" y1="0" x2="1" y2="0">
        <stop offset="0" stop-color="#8cb14b" stop-opacity="0"/>
        <stop offset="0.45" stop-color="#8cb14b" stop-opacity="0.3"/>
        <stop offset="1" stop-color="#8cb14b" stop-opacity="0.75"/>
      </linearGradient>
    </defs>
    <rect x="0" y="0" width="400" height="683" fill="url(#emblemTone)"/>
  </svg>

  <div class="name">Rosalind K Whitcombe</div>

  <div class="credentials">
    <div>BSN/RN Case Manager</div>
    <div>BA/Sociology</div>
  </div>

  <div class="contact-line cell">
    <svg class="contact-icon" viewBox="0 0 50 58" aria-hidden="true">
      <rect x="24" y="0" width="3" height="10" fill="var(--green)"/>
      <rect x="10" y="8" width="22" height="50" rx="3" fill="var(--green)"/>
      <rect x="13" y="12" width="16" height="13" fill="var(--paper)"/>
      <g fill="var(--paper)">
        <rect x="13" y="29" width="4" height="4"/><rect x="19" y="29" width="4" height="4"/><rect x="25" y="29" width="4" height="4"/>
        <rect x="13" y="36" width="4" height="4"/><rect x="19" y="36" width="4" height="4"/><rect x="25" y="36" width="4" height="4"/>
        <rect x="13" y="43" width="4" height="4"/><rect x="19" y="43" width="4" height="4"/><rect x="25" y="43" width="4" height="4"/>
      </g>
    </svg>
    <span>817-306-1597</span>
  </div>

  <div class="contact-line home">
    <svg class="contact-icon" viewBox="0 0 50 58" aria-hidden="true">
      <path d="M2 18 Q25 6 48 18 L46 25 L38 23 L37 18 Q25 14 13 18 L12 23 L4 25 Z" fill="var(--green)"/>
      <path d="M14 24 L36 24 L44 44 L6 44 Z" fill="var(--green)"/>
      <circle cx="25" cy="34" r="6" fill="var(--paper)"/>
      <circle cx="25" cy="34" r="3" fill="var(--green)"/>
    </svg>
    <span>817-492-0618</span>
  </div>
</div>
</body>
</html>
```